"Trade with Tilly" needs a funky and stylish business card

Hi my name is Tilly, I am an experienced Bidlo Gold Trader with a 100% satisfaction rating and over 400 items sold

My business name and bidlo username is "Trade with Tilly" I sell other peoples items on Bidlo for a commission. The main items I sell are furniture and renovation/building salvage items such as used kitchens, bathrooms , window doors etc.

I will be promoting my service in real estate agent offices, storage facilities, removalists, building and renovating companies.

i believe selling on bidlo is a great way for people to recycle their used goods and salvageable materials and reduce waste and landfill.

Target Market(s)

people selling their homes, renovators, builders, downsizers

Industry/Entity Type

Real Estate

Contact Information for Business Card

Tilly Marchbank
0472906147

Logo Text

Trade with Tilly

Logo styles of interest
Wordmark Logo
Requirements
Must have
• the business card must feature the bidlo logo mentioning goldtraderr top rated seller I have attached a copy
Nice to have
• i would like to have the trade with tilly logo written in royal blue

```html
<!DOCTYPE html>
<html lang="en">
<head>
<meta charset="utf-8">
<title>Trade with Tilly – Business Card</title>
<link rel="stylesheet" href="https://fonts.googleapis.com/css2?family=Roboto:wght@400;500;700;900&display=swap">
<style>
  :root {
    --bg: #2b2b2b;
    --card-top: #ffffff;
    --card-bottom: #ececec;
    --royal-blue: #1d6fc4;
    --royal-blue-dark: #0f4f9a;
    --ink: #3a3a3a;
    --ink-soft: #555555;
    --label-blue: #2a7fd0;
    --badge-gold: #e9b824;
    --badge-navy: #2a3f9e;
  }
  * { box-sizing: border-box; margin: 0; padding: 0; }
  html, body {
    width: 1200px; height: 1000px; overflow: hidden;
    background: var(--bg);
    font-family: "Roboto", Arial, sans-serif;
  }
  .canvas {
    position: relative; width: 1200px; height: 1000px;
    display: flex; flex-direction: column; align-items: center; justify-content: center; gap: 36px;
  }
  .card {
    position: relative; width: 780px; height: 446px;
    background: linear-gradient(180deg, var(--card-top) 0%, #f7f7f7 48%, var(--card-bottom) 52%, #f4f4f4 100%);
    overflow: hidden;
  }

  /* Back: contact side */
  .card--contact .brand-row {
    position: absolute; top: 58px; left: 0; right: 0;
    display: flex; justify-content: center; align-items: center; gap: 60px;
  }
  .marketplace {
    display: flex; align-items: center; gap: 14px;
  }
  .marketplace__badge { width: 44px; height: 44px; }
  .marketplace__name {
    font-weight: 700; font-size: 64px; color: var(--label-blue); letter-spacing: -1px;
  }
  .marketplace__tier { width: 30px; height: 30px; align-self: flex-start; margin-top: 6px; }
  .wordmark--small {
    font-weight: 900; font-size: 40px; color: var(--royal-blue); line-height: 1;
    text-transform: uppercase; letter-spacing: 0.5px;
  }
  .contact {
    position: absolute; top: 190px; left: 0; right: 0; text-align: center; color: var(--ink);
  }
  .contact__name { font-size: 26px; font-weight: 400; margin-bottom: 6px; }
  .contact__line { font-size: 15px; color: var(--ink-soft); line-height: 1.45; }
  .contact__label { color: var(--label-blue); font-weight: 500; }
  .services {
    position: absolute; bottom: 62px; left: 0; right: 0; text-align: center;
    font-size: 25px; font-weight: 500; color: var(--ink); line-height: 1.2;
  }

  /* Front: logo side */
  .card--logo { display: flex; align-items: center; justify-content: center; }
  .wordmark--large {
    font-weight: 900; font-size: 104px; color: var(--royal-blue); line-height: 0.95;
    text-transform: uppercase; text-align: center; letter-spacing: 1px;
  }
</style>
</head>
<body>
<main class="canvas">

  <section class="card card--contact" aria-label="Business card, contact side">
    <div class="brand-row">
      <div class="marketplace">
        <svg class="marketplace__badge" viewBox="0 0 44 44" aria-hidden="true">
          <circle cx="22" cy="22" r="20" fill="var(--badge-gold)"/>
        </svg>
        <span class="marketplace__name">Bidlo</span>
        <svg class="marketplace__tier" viewBox="0 0 30 30" aria-hidden="true">
          <rect x="3" y="3" width="24" height="24" fill="var(--badge-navy)"/>
        </svg>
      </div>
      <div class="wordmark--small">Trade with<br>Tilly</div>
    </div>

    <div class="contact">
      <p class="contact__name">Tilly Marchbank</p>
      <p class="contact__line"><span class="contact__label">bidlo user:</span> Trade with Tilly</p>
      <p class="contact__line"><span class="contact__label">tel:</span> 0472 906 147</p>
    </div>

    <p class="services">deceased estate - renovation salvage<br>furniture - building materials - collectables</p>
  </section>

  <section class="card card--logo" aria-label="Business card, logo side">
    <h1 class="wordmark--large">Trade with<br>Tilly</h1>
  </section>

</main>
</body>
</html>
```